Medspa business needs a webpage

we need a website for a new Medspa company based in Lynden, WA called Lumara Vale Medical Aesthetics. We offer non surgical, cosmetic procedures as well as medical weight loss. We would like a sleek design, with rich colors (dark, emerald green and gold). The website should list our services, pricing and links to book appointments.

```html
<!DOCTYPE html>
<html lang="en">
<head>
<meta charset="utf-8">
<title>Lumara Vale Medical Aesthetics</title>
<link rel="stylesheet" href="https://fonts.googleapis.com/css2?family=Gilda+Display&family=DM+Sans:wght@400;500;700&display=swap">
<style>
:root{
  --ink:#050f01;
  --forest:#0a1e02;
  --gold:#bfa147;
  --mist:#e1e2e3;
  --paper:#f7f8f9;
  --stage:#d6d6d6;
  --serif:"Gilda Display", Georgia, serif;
  --sans:"DM Sans", Arial, sans-serif;
}
*{margin:0;padding:0;box-sizing:border-box}
html,body{width:1200px;height:3735px;overflow:hidden;background:var(--stage)}
.site{position:absolute;left:245px;top:278px;width:710px;height:3331px;background:var(--forest);overflow:hidden;font-family:var(--sans);color:var(--paper)}
.abs{position:absolute}
.serif{font-family:var(--serif);font-weight:400;line-height:1.05}
.gold{color:var(--gold)}
.white{color:var(--paper)}
em{font-style:italic}
.body{font-size:8px;line-height:1.6;color:var(--mist)}
.btn{position:absolute;display:inline-flex;align-items:center;gap:5px;background:var(--gold);color:var(--ink);font-size:7px;font-weight:500;border-radius:12px;padding:5px 10px;white-space:nowrap}
.btn svg,.nav-book svg{width:8px;height:8px;flex:none}
.photo{position:absolute}

/* nav */
.nav{position:absolute;left:0;top:0;width:710px;height:38px;background:var(--forest)}
.brand{position:absolute;display:flex;align-items:center;gap:6px;font-family:var(--serif);color:var(--gold);letter-spacing:2px;text-transform:uppercase;white-space:nowrap}
.brand .dot{width:9px;height:9px;border-radius:50%;background:var(--gold)}
.nav-links{position:absolute;left:230px;top:15px;display:flex;gap:28px;font-size:7px;color:var(--mist)}
.nav-book{position:absolute;left:503px;top:9px;border:1px solid var(--gold);border-radius:12px;padding:5px 10px;font-size:7px;display:flex;gap:5px;align-items:center;white-space:nowrap;color:var(--paper)}
.nav-call{position:absolute;left:609px;top:8px;width:21px;height:21px;border-radius:50%;background:var(--gold);display:flex;align-items:center;justify-content:center}

/* hero */
.hero-panel{left:0;top:38px;width:277px;height:397px;background:linear-gradient(135deg,#0d2205,#061201)}
.hero-photo{left:277px;top:38px;width:433px;height:397px;border-bottom-right-radius:22px;background:linear-gradient(120deg,#2a211b 0%,#6b5748 35%,#b49a88 60%,#d9c8bc 100%)}
.hero-card{left:80px;top:101px;width:280px;height:271px;background:var(--paper);border-radius:14px;color:var(--ink)}
.hero-card h1{position:absolute;left:32px;top:28px;font-size:35px;line-height:1.04;color:var(--ink)}
.hero-card p{position:absolute;left:32px;top:154px;font-size:7.5px;color:#4a4a4a}

/* services */
.svc-title{font-size:25px}
.svc-icon{position:absolute;width:36px;height:36px}

/* team */
.team{left:0;top:961px;width:710px;height:604px;background:var(--ink);border-radius:18px}
.caption{position:absolute;font-size:7.5px;font-weight:500;color:var(--paper)}
.sec-title{font-size:26px}

/* testimonials */
.quote{font-size:9.5px;line-height:1.55;color:var(--mist)}

/* work */
.work{left:0;top:1898px;width:710px;height:468px;background:var(--paper);border-radius:20px}
.work h2{position:absolute;left:0;width:710px;top:50px;text-align:center;font-size:30px;color:var(--ink)}
.compare{position:absolute;left:78px;top:138px;width:552px;height:268px;border-radius:14px;overflow:hidden}
.compare .half{position:absolute;top:0;height:268px;width:276px}

/* pricing */
.tabs{position:absolute;left:80px;top:2540px;display:flex;gap:28px;font-size:7.5px}
.tabs span{color:#7d8a6e}
.tabs .on{color:var(--paper);font-weight:500}
.price-col{position:absolute;top:2580px;width:267px}
.row{display:flex;justify-content:space-between;font-family:var(--serif);font-size:10.5px;height:36.5px;padding-top:7px;border-top:1px solid rgba(225,226,227,.12)}
.row .amt{color:var(--gold)}

/* cta */
.cta{left:0;top:2830px;width:710px;height:224px;background:linear-gradient(160deg,#0c2204,#061401);border-radius:20px}
.cta h2{position:absolute;left:0;width:710px;top:72px;text-align:center;font-size:30px;line-height:1.05}

/* footer */
.foot-label{font-size:6.5px;color:#8f9a80;margin-bottom:8px}
.foot-item{font-size:6.5px;color:var(--paper);margin-bottom:9px;font-weight:500;white-space:nowrap}
.social{position:absolute;top:3189px;width:18px;height:18px;border-radius:50%;background:var(--gold)}
</style>
</head>
<body>
<main class="site">

  <header class="nav">
    <div class="brand" style="left:80px;top:14px;font-size:8.5px"><span class="dot"></span>Lumara Vale</div>
    <nav class="nav-links"><span>Services</span><span>About</span><span>Pricing</span></nav>
    <div class="nav-book">Book an Appointment
      <svg viewBox="0 0 10 10" fill="none" stroke="#f7f8f9" stroke-width="1"><rect x="1" y="2" width="8" height="7" rx="1"/><path d="M1 4.5h8M3 1v2M7 1v2"/></svg></div>
    <div class="nav-call"><svg width="11" height="11" viewBox="0 0 24 24" fill="none" stroke="#050f01" stroke-width="2"><path d="M5 3h4l2 5-3 2a12 12 0 0 0 6 6l2-3 5 2v4a2 2 0 0 1-2 2A17 17 0 0 1 3 5a2 2 0 0 1 2-2z"/></svg></div>
  </header>

  <div class="abs hero-panel" role="img" aria-label="Dark green panel with soft leaf texture"></div>
  <div class="photo hero-photo" role="img" aria-label="Photo of a client receiving a facial mask applied with a fan brush"></div>
  <section class="abs hero-card">
    <h1 class="serif">Going extra<br>&nbsp;grin for your<br>perfect skin</h1>
    <p>Experience comfort-driven care and stunning results</p>
    <span class="btn" style="left:32px;top:212px">Book an Appointment
      <svg viewBox="0 0 10 10" fill="none" stroke="#050f01" stroke-width="1"><rect x="1" y="2" width="8" height="7" rx="1"/><path d="M1 4.5h8M3 1v2M7 1v2"/></svg></span>
  </section>

  <h2 class="abs serif svc-title gold" style="left:164px;top:493px">Non-Surgical<br>&nbsp;&nbsp;Service</h2>
  <svg class="svc-icon" style="left:125px;top:572px" viewBox="0 0 36 36" fill="none" stroke="#bfa147" stroke-width="1.3"><circle cx="20" cy="14" r="8"/><path d="M14 20l-9 12M20 22v6M26 19l4 4"/><path d="M4 10l2-2M30 6l2-2"/></svg>
  <p class="abs body" style="left:180px;top:566px;width:170px">Enhance your look without surgery using safe, minimally invasive treatments and methods designed to refresh, rejuvenate, natural beauty with minimal downtime.</p>

  <h2 class="abs serif svc-title gold" style="left:430px;top:602px">Cosmetic<br>&nbsp;&nbsp;Procedures</h2>
  <svg class="svc-icon" style="left:393px;top:680px" viewBox="0 0 36 36" fill="none" stroke="#bfa147" stroke-width="1.3"><path d="M12 6h14l4 10-4 14H14L10 16z"/><path d="M17 16h4M19 16v6"/><path d="M4 26l2 2-2 2-2-2zM32 4l1.5 1.5L32 7l-1.5-1.5z"/></svg>
  <p class="abs body" style="left:446px;top:672px;width:145px">Target wrinkles, fine lines, and other skin concerns through advanced cosmetic procedures that improve your appearance.</p>

  <h2 class="abs serif svc-title gold" style="left:213px;top:766px">Medical<br>&nbsp;&nbsp;Weight-Loss</h2>
  <svg class="svc-icon" style="left:168px;top:838px" viewBox="0 0 36 36" fill="none" stroke="#bfa147" stroke-width="1.3"><path d="M10 4c2 6 2 10 0 14s0 12 2 14M26 4c-2 6-2 10 0 14s0 12-2 14"/><path d="M3 18h6M7 16l2 2-2 2M33 18h-6M29 16l-2 2 2 2M10 10h16"/></svg>
  <p class="abs body" style="left:229px;top:835px;width:175px">Follow personalized programs and expert guidance for safe and effective weight loss, supporting healthier habits, boosting energy, and helping you reach your wellness goals.</p>

  <section class="abs team"></section>
  <div class="photo" style="left:433px;top:797px;width:277px;height:215px;border-top-left-radius:14px;background:linear-gradient(160deg,#9aa19a,#6e746c 55%,#2b2a28)" role="img" aria-label="Portrait photo of a smiling skincare specialist"></div>
  <span class="caption" style="left:455px;top:1026px">Mira - Skincare Specialist</span>
  <div class="photo" style="left:57px;top:947px;width:233px;height:183px;border-radius:12px;background:linear-gradient(160deg,#a9adab,#7a7d7b 55%,#2a2624)" role="img" aria-label="Portrait photo of a smiling skincare specialist"></div>
  <span class="caption" style="left:78px;top:1144px">Mira - Skincare Specialist</span>

  <h2 class="abs serif sec-title gold" style="left:374px;top:1106px">A professional<br>&nbsp;&nbsp;&nbsp;and <em class="white">experienced</em><br>&nbsp;team that cares</h2>
  <p class="abs body" style="left:391px;top:1198px;width:180px">Our specialists combine expertise, compassion, and personalized care to help every client feel confident and comfortable.</p>

  <h2 class="abs serif sec-title gold" style="left:78px;top:1234px">A care that feels<br>&nbsp;&nbsp;&nbsp;<em class="white">thoughtful</em>, and<br>not rushed</h2>
  <p class="abs body" style="left:94px;top:1325px;width:180px">We provide personalized attention in a calm, relaxed environment, ensuring every treatment feels deliberate, comfortable, and tailored to you.</p>

  <div class="photo" style="left:312px;top:1284px;width:124px;height:114px;border-radius:50%;background:radial-gradient(circle at 45% 40%,#f4ead8,#c9ab7a 55%,#050f01 72%)" role="img" aria-label="Photo of an open jar of cream"></div>

  <h2 class="abs serif sec-title gold" style="left:459px;top:1377px">A consistent<br>&nbsp;&nbsp;&nbsp;<em class="white">care</em> you can<br>count on.</h2>
  <p class="abs body" style="left:480px;top:1469px;width:160px">We provide thoughtful, consistent attention, making sure every visit feels smooth and truly focused on you.</p>

  <h2 class="abs serif gold" style="left:80px;top:1582px;font-size:30px">What <span class="white">people</span><br>&nbsp;&nbsp;say about our<br>work</h2>
  <span class="btn" style="left:535px;top:1661px;font-size:6.5px">See Our Verified Reviews</span>
  <p class="abs quote" style="left:224px;top:1714px;width:345px">“What stood out most was how clean and inviting the clinic was. The team’s attention to hygiene and detail made me feel completely safe and relaxed during my skin treatment.”</p>
  <div class="photo" style="left:226px;top:1784px;width:34px;height:34px;border-radius:50%;background:radial-gradient(circle,#e4c6ad,#a77f62)" role="img" aria-label="Reviewer photo"></div>
  <span class="abs gold" style="left:267px;top:1797px;font-size:7px">Corinne Ashby</span>
  <svg class="abs" style="left:80px;top:1826px" width="40" height="12" viewBox="0 0 40 12" fill="none" stroke="#f7f8f9" stroke-width="1.2"><path d="M11 6H2M6 2L2 6l4 4"/><path d="M26 6h9M31 2l4 4-4 4"/></svg>

  <section class="abs work">
    <h2 class="serif">We are <em class="gold">proud</em> to present<br>our work</h2>
    <div class="compare">
      <div class="half" style="left:0;background:linear-gradient(110deg,#1a1310,#6a4a3a 45%,#a47b63 80%,#8c6652)" role="img" aria-label="Before photo of skin with visible texture"></div>
      <div class="half" style="left:276px;background:linear-gradient(250deg,#0d0b0a,#6a4c3e 40%,#b8917a 80%,#a27e69)" role="img" aria-label="After photo of smoother skin"></div>
      <div class="abs" style="left:275px;top:0;width:2px;height:268px;background:var(--paper)"></div>
      <div class="abs" style="left:262px;top:120px;width:28px;height:28px;border-radius:50%;background:var(--paper);display:flex;align-items:center;justify-content:center">
        <svg width="14" height="8" viewBox="0 0 14 8" fill="none" stroke="#050f01" stroke-width="1.2"><path d="M4 1L1 4l3 3M10 1l3 3-3 3"/></svg></div>
    </div>
  </section>

  <h2 class="abs serif white" style="left:80px;top:2410px;font-size:26px;line-height:1.05">Transparent <span class="gold">and</span><br>&nbsp;&nbsp;&nbsp;affordable <span class="gold">pricings</span><br><span class="gold">for every skin goal.</span></h2>
  <p class="abs body" style="left:389px;top:2425px;width:245px">We offer clear, upfront pricing on all services so you can plan your treatments with confidence. No hidden fees—just professional care that fits your budget.</p>
  <span class="btn" style="left:389px;top:2482px">Book an Appointment
    <svg viewBox="0 0 10 10" fill="none" stroke="#050f01" stroke-width="1"><rect x="1" y="2" width="8" height="7" rx="1"/><path d="M1 4.5h8M3 1v2M7 1v2"/></svg></span>
  <div class="tabs"><span class="on">Non-Surgical</span><span>Cosmetic Procedures</span><span>Medical Weight-Loss</span></div>
  <div class="price-col" style="left:80px">
    <div class="row"><span>Neurotoxin &amp; Dermal Fillers</span><span class="amt">$25</span></div>
    <div class="row"><span>Laser Skin Rejuvenation</span><span class="amt">$85</span></div>
    <div class="row"><span>PRP (Platelet-Rich Plasma) Therapy</span><span class="amt">$35</span></div>
    <div class="row"><span>Cryolipolysis / Fat Reduction</span><span class="amt">$50</span></div>
  </div>
  <div class="price-col" style="left:363px">
    <div class="row"><span>Microneedling</span><span class="amt">$20</span></div>
    <div class="row"><span>Chemical Peels</span><span class="amt">$25</span></div>
    <div class="row"><span>Non-Surgical Facelift</span><span class="amt">$80</span></div>
    <div class="row"><span>Skin Hydration Therapy</span><span class="amt">$75</span></div>
  </div>

  <section class="abs cta">
    <h2 class="serif white">Ready for a radiant skin?<br>Book now in under <span class="gold">60 seconds.</span></h2>
    <span class="btn" style="left:305px;top:181px">Book an Appointment
      <svg viewBox="0 0 10 10" fill="none" stroke="#050f01" stroke-width="1"><rect x="1" y="2" width="8" height="7" rx="1"/><path d="M1 4.5h8M3 1v2M7 1v2"/></svg></span>
  </section>
  <div class="photo" style="left:28px;top:2756px;width:158px;height:109px;border-radius:10px;background:linear-gradient(135deg,#e9e3dc,#b9a79a 50%,#2b2622)" role="img" aria-label="Photo of a specialist giving a facial treatment"></div>
  <div class="photo" style="left:552px;top:2815px;width:88px;height:63px;border-radius:14px;background:linear-gradient(120deg,#f1ddc8,#d6a888 60%,#8e6448)" role="img" aria-label="Photo of a client using a facial roller"></div>

  <div class="brand" style="left:80px;top:3134px;font-size:10px"><span class="dot"></span>Lumara Vale</div>
  <p class="abs serif white" style="left:315px;top:3118px;width:320px;font-size:13px;line-height:1.3">A trusted, reliable, and long-standing approach to personalized MedSpa care.</p>
  <span class="social" style="left:80px"></span>
  <span class="social" style="left:103px"></span>
  <div class="abs" style="left:315px;top:3189px"><p class="foot-label">Working Hours</p><p class="foot-item">Mon–Fri 8am – 9pm</p></div>
  <div class="abs" style="left:414px;top:3189px"><p class="foot-label">Services</p><p class="foot-item">Non-Surgical</p><p class="foot-item">Cosmetic Procedures</p><p class="foot-item">Medical Weight Loss</p></div>
  <div class="abs" style="left:522px;top:3189px"><p class="foot-label">Contact Info</p><p class="foot-item">info@lumaravale.com</p><p class="foot-item">+1 360 555 0148</p></div>
  <span class="btn" style="left:522px;top:3246px">Book an Appointment
    <svg viewBox="0 0 10 10" fill="none" stroke="#050f01" stroke-width="1"><rect x="1" y="2" width="8" height="7" rx="1"/><path d="M1 4.5h8M3 1v2M7 1v2"/></svg></span>
  <p class="abs" style="left:80px;top:3254px;font-size:5.5px;color:#8f9a80">2025 © Lumara Vale | Privacy Policy</p>

</main>
</body>
</html>
```